Flyer design for the Harvest Of Light Summit 2019 (HOLUMN)

Design a flyer for our annual conference with basic information about the conference: conference logo and year, Conference name: Harvest Of Light Summit Location: Tallow Community Center (Downtown Portland)382 Wimbrel Lane, Portland, ME 04107, Date: August 8th, 9th, 10th and 11th, 2019Start time 7:00PMI would like the following three words added to the flyer. These words describe the vision of the conference: Prophetic, Fire, Overflow,

Contact info:
Website: www.quentavo.org
Phone: 207 555 0143
Email: contact@plumvesta.org

Target Market(s)

Young adults living in the United States

Industry/Entity Type

Religious

Font styles to use
Sans Serif

Colors

Designer to choose colors to be used in the design.

Requirements
Must have
• HOLUMN must logo standout, the reader should be able to take a quick look and find key info,
Should not have
• Cross image, church image

```html
<!DOCTYPE html>
<html lang="en">
<head>
<meta charset="utf-8">
<title>HOLUMN 2019 – Harvest Of Light Summit</title>
<link rel="stylesheet" href="https://fonts.googleapis.com/css2?family=Montserrat:wght@700;800&family=Roboto+Condensed:wght@300;400;700&display=swap">
<style>
  :root {
    --ink: #000000;
    --blue: #1a74c2;
    --blue-soft: #4a86cf;
    --orange: #f7941d;
    --white: #ffffff;
  }
  * { margin: 0; padding: 0; box-sizing: border-box; }
  html, body { width: 927px; height: 1200px; overflow: hidden; background: var(--ink); }
  .flyer {
    position: relative;
    width: 927px;
    height: 1200px;
    background: var(--ink);
    font-family: "Roboto Condensed", "Arial Narrow", sans-serif;
    color: var(--white);
    text-align: center;
  }
  .artwork {
    position: absolute;
    top: 384px; left: 0;
    width: 927px; height: 580px;
  }
  .event-name {
    position: absolute;
    top: 50px; left: 0; right: 0;
    font-size: 40px;
    font-weight: 400;
    line-height: 48px;
    color: var(--blue);
    text-transform: uppercase;
    letter-spacing: 1px;
  }
  .brand {
    position: absolute;
    top: 112px; left: 0; right: 0;
    font-family: "Montserrat", sans-serif;
    font-weight: 800;
    font-size: 132px;
    line-height: 1;
    color: var(--blue);
    letter-spacing: 2px;
  }
  .year {
    position: absolute;
    top: 250px; left: 170px; width: 610px;
    display: flex; align-items: center; gap: 18px;
    font-family: "Montserrat", sans-serif;
    font-weight: 700;
    font-size: 52px;
    line-height: 56px;
    color: var(--orange);
    letter-spacing: 26px;
  }
  .year .rule { flex: 1; height: 4px; background: var(--orange); }
  .year .digits { margin-right: -26px; }
  .vision {
    position: absolute;
    top: 322px; left: 0; right: 0;
    font-size: 62px;
    line-height: 72px;
    font-weight: 400;
    text-transform: uppercase;
    color: var(--blue);
  }
  .vision .fire, .vision .sep { color: var(--orange); }
  .vision .sep { margin: 0 24px; }
  .dates {
    position: absolute;
    top: 898px; left: 132px;
    width: 668px; height: 132px;
    border: 2px solid var(--orange);
  }
  .dates .month {
    position: absolute;
    top: -34px; left: 50%;
    transform: translateX(-50%);
    padding: 0 20px;
    background: var(--ink);
    font-size: 74px;
    font-weight: 300;
    line-height: 62px;
    color: var(--white);
  }
  .dates .days {
    position: absolute;
    top: 36px; left: 0; right: 0;
    font-size: 46px;
    line-height: 50px;
    font-weight: 700;
  }
  .dates .days sup { font-size: 23px; font-weight: 400; vertical-align: 18px; }
  .dates .days .and { font-size: 23px; font-weight: 400; margin: 0 6px; }
  .dates .start {
    position: absolute;
    bottom: -18px; left: 50%;
    transform: translateX(-50%);
    padding: 0 22px;
    background: var(--ink);
    font-size: 29px;
    line-height: 34px;
    color: var(--blue-soft);
    white-space: nowrap;
  }
  .venue {
    position: absolute;
    top: 1058px; left: 0; right: 0;
    font-size: 21px;
    font-style: normal;
    line-height: 26px;
    color: var(--orange);
    text-transform: uppercase;
  }
  .contact {
    position: absolute;
    top: 1131px; left: 107px; right: 84px;
    display: flex; justify-content: space-between;
    font-size: 17px;
    color: var(--blue-soft);
    text-transform: uppercase;
  }
</style>
</head>
<body>
<main class="flyer">
  <svg class="artwork" viewBox="0 0 927 580" role="img" aria-label="Photo of a splash of water colliding with a burst of flame">
    <defs>
      <radialGradient id="waterGlow" cx="0.5" cy="0.5" r="0.5">
        <stop offset="0" stop-color="#9fc3e0" stop-opacity="0.5"/>
        <stop offset="0.6" stop-color="#3c5f80" stop-opacity="0.22"/>
        <stop offset="1" stop-color="#000" stop-opacity="0"/>
      </radialGradient>
      <radialGradient id="fireGlow" cx="0.5" cy="0.5" r="0.5">
        <stop offset="0" stop-color="#f7a030" stop-opacity="0.9"/>
        <stop offset="0.45" stop-color="#e8561a" stop-opacity="0.6"/>
        <stop offset="0.8" stop-color="#7a1208" stop-opacity="0.3"/>
        <stop offset="1" stop-color="#000" stop-opacity="0"/>
      </radialGradient>
    </defs>
    <rect width="927" height="580" fill="#000"/>
    <ellipse cx="250" cy="320" rx="320" ry="230" fill="url(#waterGlow)"/>
    <ellipse cx="650" cy="320" rx="360" ry="240" fill="url(#fireGlow)"/>
  </svg>

  <p class="event-name">Harvest Of Light Summit</p>
  <h1 class="brand">HOLUMN</h1>
  <div class="year"><span class="rule"></span><span class="digits">2019</span><span class="rule"></span></div>
  <p class="vision">Prophetic<span class="sep">|</span><span class="fire">Fire</span><span class="sep">|</span>Overflow</p>

  <section class="dates">
    <span class="month">AUGUST</span>
    <p class="days">8<sup>TH</sup>, 9<sup>TH</sup>, 10<sup>TH</sup><span class="and">AND</span>11<sup>TH</sup>, 2019</p>
    <span class="start">START TIME 7:00PM</span>
  </section>

  <address class="venue">
    Tallow Community Center (Downtown Portland)<br>
    382 Wimbrel Lane, Portland, ME 04107
  </address>

  <footer class="contact">
    <span>Phone: 207 555 0143</span><span>|</span>
    <span>Email: contact@plumvesta.org</span><span>|</span>
    <span>www.quentavo.org</span>
  </footer>
</main>
</body>
</html>
```